Lobby Sentinel Staffing

Lobby sentinel is similar to a security company but is more concierge/customer service oriented. Picture a security guard in a suit working at a condo or office building. Our thoughts for a logo is a silhouette of a male/female sitting at a desk or some type of crest but were open to creative ideas.

Target Market(s)

Property Managers

Industry/Entity Type

Security

Font styles to use
Serif

Requirements
Must have
• Male/Female sitting professionally at a desk.
Nice to have
• Vertical card
Should not have
• Cartoons

```html
<!DOCTYPE html>
<html lang="en">
<head>
<meta charset="utf-8">
<title>Lobby Sentinel Staffing – Business Card</title>
<link rel="stylesheet" href="https://fonts.googleapis.com/css2?family=Tinos:wght@400;700&display=swap">
<style>
  :root {
    --backdrop: #e9e6e1;
    --card-white: #ffffff;
    --card-shade: #eef0f3;
    --brand-blue: #1f63a8;
    --brand-blue-deep: #124b86;
    --brand-blue-light: #3a82c4;
    --stripe-grey: #c9ced6;
    --address-blue: #4e7aa6;
    --text-light: #ffffff;
  }
  * { box-sizing: border-box; margin: 0; padding: 0; }
  html, body {
    width: 1200px; height: 1023px; overflow: hidden;
    background: var(--backdrop);
    font-family: "Tinos", "Times New Roman", serif;
  }
  .business-card {
    position: absolute; left: 350px; top: 82px;
    width: 500px; height: 860px;
    background: linear-gradient(180deg, var(--card-white) 0%, var(--card-shade) 100%);
    box-shadow: 0 10px 30px rgba(0,0,0,.18);
    overflow: hidden;
  }
  .card-shapes { position: absolute; inset: 0; }
  .brand-block {
    position: absolute; top: 60px; left: 0; width: 100%;
    display: flex; flex-direction: column; align-items: center; gap: 26px;
  }
  .brand-dot {
    width: 150px; height: 150px; border-radius: 50%;
    background: var(--brand-blue);
  }
  .brand-name {
    font-size: 36px; font-weight: 400; color: var(--brand-blue-deep);
    letter-spacing: 1px;
  }
  .contact-block {
    position: absolute; top: 470px; left: 0; width: 100%;
    color: var(--text-light);
  }
  .person-name {
    text-align: center; font-size: 30px; font-weight: 700; padding-left: 40px;
  }
  .person-role {
    text-align: center; font-size: 17px; margin-top: 4px; padding-left: 80px;
  }
  .contact-list {
    list-style: none; margin-top: 26px; padding-left: 60px;
    display: flex; flex-direction: column; gap: 10px;
    font-size: 19px; letter-spacing: 1px;
  }
  .contact-list li { display: flex; align-items: center; gap: 12px; }
  .contact-list li.phone { padding-left: 64px; font-size: 21px; }
  .contact-icon { width: 18px; height: 18px; flex: none; }
  .address-block {
    position: absolute; right: 40px; bottom: 50px;
    display: flex; align-items: center; gap: 18px;
    color: var(--address-blue); font-size: 22px; letter-spacing: 1.5px;
  }
  .address-lines { text-align: right; line-height: 1.4; font-style: normal; }
  .pin-badge { width: 46px; height: 46px; }
</style>
</head>
<body>
  <article class="business-card">
    <svg class="card-shapes" viewBox="0 0 500 860" aria-hidden="true">
      <defs>
        <linearGradient id="bandFill" x1="0" y1="0" x2="1" y2="1">
          <stop offset="0" stop-color="#3a82c4"/>
          <stop offset="1" stop-color="#124b86"/>
        </linearGradient>
      </defs>
      <path d="M0 420 C 150 395, 320 375, 500 345 L 500 700 C 330 680, 150 700, 0 790 Z" fill="url(#bandFill)"/>
      <path d="M0 420 C 150 395, 320 375, 500 345 L 500 358 C 320 388, 150 408, 0 432 Z" fill="var(--brand-blue-deep)"/>
      <path d="M0 790 C 150 700, 330 680, 500 700 L 500 712 C 330 694, 160 712, 0 802 Z" fill="var(--stripe-grey)"/>
    </svg>

    <header class="brand-block">
      <span class="brand-dot"></span>
      <h1 class="brand-name">Lobby Sentinel Staffing</h1>
    </header>

    <section class="contact-block">
      <h2 class="person-name">Marian Whitlock</h2>
      <p class="person-role">Director</p>
      <ul class="contact-list">
        <li class="phone">
          <svg class="contact-icon" viewBox="0 0 24 24"><path fill="#fff" d="M6.6 10.8a15 15 0 0 0 6.6 6.6l2.2-2.2a1 1 0 0 1 1-.25 11.4 11.4 0 0 0 3.6.57 1 1 0 0 1 1 1V20a1 1 0 0 1-1 1A17 17 0 0 1 3 4a1 1 0 0 1 1-1h3.5a1 1 0 0 1 1 1c0 1.250.2 2.45.57 3.57a1 1 0 0 1-.25 1z"/></svg>
          <span>555-014-2280</span>
        </li>
        <li class="email">
          <svg class="contact-icon" viewBox="0 0 24 24"><rect x="2" y="5" width="20" height="14" rx="2" fill="#fff"/><path d="M3 6l9 7 9-7" stroke="#1f63a8" stroke-width="2" fill="none"/></svg>
          <span>marianwhitlock@mailbox.com</span>
        </li>
        <li class="web">
          <svg class="contact-icon" viewBox="0 0 24 24"><rect x="3" y="4" width="18" height="16" rx="2" fill="#fff"/><path d="M3 9h18M8 12h2M12 12h2M16 12h2M8 15h2M12 15h2M16 15h2" stroke="#1f63a8" stroke-width="1.5"/></svg>
          <span>www.lobbysentinelstaffing.com</span>
        </li>
      </ul>
    </section>

    <footer class="address-block">
      <svg class="pin-badge" viewBox="0 0 46 46" aria-hidden="true">
        <circle cx="23" cy="23" r="21" fill="none" stroke="#4e7aa6" stroke-width="2"/>
        <path d="M23 11a7 7 0 0 0-7 7c0 5 7 13 7 13s7-8 7-13a7 7 0 0 0-7-7z" fill="#4e7aa6"/>
        <circle cx="23" cy="18" r="2.6" fill="#fff"/>
      </svg>
      <address class="address-lines">
        PO Box 5127 Elkhorn<br>WY 8206
      </address>
    </footer>
  </article>
</body>
</html>
```